Brightwater Commerce Business Card Design

Hello,

Attached you will find our logo. We are looking for a sharp business card design.

Other info to be included is:
Name: Marcus Delaney
Title: CEO
Office: (555) 382-7146
Cell: (555) 382-7146
E-mail address: marcus@brightwatercommerce.example
website: www.BrightwaterCommerce.example

```html
<!DOCTYPE html>
<html lang="en">
<head>
<meta charset="UTF-8">
<title>Brightwater Commerce Business Card</title>
<link href="https://fonts.googleapis.com/css2?family=Open+Sans:wght@400;700&display=swap" rel="stylesheet">
<style>
  :root {
    --page-bg: #e9e7e4;
    --card-bg: #ffffff;
    --card-edge: #dcdcdc;
    --ink-dark: #2e2e2e;
    --ink-body: #3a3a3a;
    --brand-blue: #2f6db3;
    --brand-red: #d8453a;
    --glow: #e6e6e6;
  }
  * { box-sizing: border-box; margin: 0; padding: 0; }
  html, body {
    width: 1200px;
    height: 1000px;
    overflow: hidden;
  }
  body {
    background: var(--page-bg);
    font-family: "Open Sans", Arial, sans-serif;
    position: relative;
  }
  .card {
    position: absolute;
    top: 357px;
    width: 500px;
    height: 286px;
    background: var(--card-bg);
    border: 1px solid var(--card-edge);
    box-shadow: 0 4px 14px rgba(0, 0, 0, 0.12);
  }
  .card--front {
    left: 70px;
    background: radial-gradient(ellipse 46% 40% at 50% 50%, var(--card-bg) 35%, var(--glow) 100%);
    background-color: var(--card-bg);
    display: flex;
    align-items: center;
    justify-content: center;
  }
  .card--front::before {
    content: "";
    position: absolute;
    inset: 0;
    background: radial-gradient(ellipse 38% 34% at 50% 50%, rgba(0,0,0,0.06), rgba(255,255,255,0) 70%), var(--card-bg);
    z-index: 0;
  }
  .brand {
    position: relative;
    z-index: 1;
    display: flex;
    align-items: center;
    gap: 10px;
  }
  .brand__mark {
    width: 14px;
    height: 14px;
    background: var(--brand-red);
  }
  .brand__name {
    font-size: 22px;
    font-weight: 700;
    color: var(--brand-blue);
    letter-spacing: 0.5px;
  }
  .card--back {
    left: 630px;
    padding: 72px 0 0 112px;
    color: var(--ink-body);
  }
  .contact__name {
    font-size: 22px;
    font-weight: 700;
    color: var(--ink-dark);
    line-height: 1.1;
  }
  .contact__title {
    font-size: 12px;
    font-weight: 700;
    color: var(--ink-dark);
    margin-bottom: 18px;
  }
  .contact__list {
    list-style: none;
    font-size: 11.5px;
    line-height: 1.45;
  }
</style>
</head>
<body>
  <section class="card card--front" aria-label="Business card front">
    <div class="brand">
      <span class="brand__mark"></span>
      <span class="brand__name">Brightwater Commerce</span>
    </div>
  </section>

  <section class="card card--back" aria-label="Business card back">
    <h1 class="contact__name">Mr. Marcus Delaney</h1>
    <p class="contact__title">CEO</p>
    <ul class="contact__list">
      <li>Office: (555) 382-7146</li>
      <li>Mobile: (555) 382-7146</li>
      <li>E-mail: marcus@brightwatercommerce.example</li>
      <li>Website: www.BrightwaterCommerce.example</li>
    </ul>
  </section>
</body>
</html>
```